Business card design and logo needed

We have been operating as Ridgeline Paddock Fencing for 30 years but never had a logo and feel there is a need for one, but have no idea for a design.
We specialise in all types of rural fencing including post and wire, post and rail, electric, chainmesh and to a lesser extent, also do industrial security fencing.
Updates

Sorry, but website is ridgelinepaddock.net

No .au on the end!
My apologies

Regards, Barry

Target Market(s)

Rural/acreage property owners, particularly horse people.

Industry/Entity Type

Industrial

Contact Information for Business Card

Ridgeline Paddock Fencing Barry Lindqvist 0427 615302. Terry Lindqvist 0427 783160
Email: ridgelinepaddock@quolmail.com.au
Website: www.ridgelinepaddock.net.au

Requirements
Must have
• Would like to highlight website address - use the business card to advertise the website or to push them to check it out.

```html
<!DOCTYPE html>
<html lang="en">
<head>
<meta charset="UTF-8">
<title>Ridgeline Paddock Fencing – Business Card</title>
<link rel="stylesheet" href="https://fonts.googleapis.com/css2?family=Arimo:wght@700&display=swap">
<style>
  :root {
    --timber-light: #dcc8ab;
    --timber-mid: #cdb593;
    --timber-dark: #b99d7a;
    --rail-brown: #3b2414;
    --band-sand: #d6c9ae;
    --ink-brown: #3b2414;
    --ink-sand: #e2d6bd;
  }
  * { margin: 0; padding: 0; box-sizing: border-box; }
  html, body { width: 1200px; height: 779px; overflow: hidden; background: #ffffff; }
  .card {
    position: relative;
    width: 1200px;
    height: 779px;
    overflow: hidden;
    font-family: "Arimo", Arial, sans-serif;
    font-weight: 700;
    color: var(--ink-brown);
  }
  .timber-backdrop {
    position: absolute;
    inset: 0;
    background:
      linear-gradient(178deg, rgba(255,255,255,0.12) 0%, rgba(0,0,0,0.04) 50%, rgba(255,255,255,0.1) 100%),
      linear-gradient(90deg, var(--timber-light) 0%, var(--timber-mid) 45%, var(--timber-light) 70%, var(--timber-dark) 100%);
  }
  .rail { position: absolute; background: var(--rail-brown); }
  .rail--top { left: 0; top: 30px; width: 1200px; height: 26px; }
  .rail--upper { left: 74px; top: 137px; width: 1126px; height: 15px; }
  .rail--post { left: 74px; top: 137px; width: 21px; height: 449px; }
  .rail--lower { left: 74px; top: 560px; width: 1126px; height: 26px; }
  .brand-name {
    position: absolute;
    font-size: 66px;
    line-height: 1;
    letter-spacing: 0.5px;
    color: var(--ink-brown);
    white-space: nowrap;
  }
  .brand-name--line1 { left: 69px; top: 70px; }
  .brand-name--line2 { left: 96px; top: 159px; }
  .contact {
    position: absolute;
    top: 342px;
    white-space: nowrap;
  }
  .contact--barry { left: 250px; }
  .contact--terry { left: 676px; }
  .contact__name { font-size: 37px; line-height: 1; }
  .contact__phone { font-size: 33px; line-height: 1; margin-top: 46px; }
  .web-band {
    position: absolute;
    left: 74px; top: 586px;
    width: 1126px; height: 72px;
    background: var(--band-sand);
    display: flex; align-items: center; justify-content: center;
    padding-right: 0;
  }
  .web-band__text { font-size: 37px; color: var(--ink-brown); transform: translateX(-50px); }
  .mail-band {
    position: absolute;
    left: 74px; top: 658px;
    width: 1126px; height: 59px;
    background: var(--rail-brown);
    display: flex; align-items: center; justify-content: center;
  }
  .mail-band__text { font-size: 28px; color: var(--ink-sand); transform: translateX(-56px); }
</style>
</head>
<body>
  <main class="card">
    <div class="timber-backdrop" role="img" aria-label="Weathered timber grain background with strands of barbed wire stretched across it"></div>

    <div class="rail rail--top"></div>
    <div class="rail rail--upper"></div>
    <div class="rail rail--post"></div>
    <div class="rail rail--lower"></div>

    <h1 class="brand">
      <span class="brand-name brand-name--line1">RIDGELINE PADDOCK</span>
      <span class="brand-name brand-name--line2">FENCING</span>
    </h1>

    <section class="contact contact--barry">
      <p class="contact__name">Barry Lindqvist</p>
      <p class="contact__phone">tel.0427 615302</p>
    </section>

    <section class="contact contact--terry">
      <p class="contact__name">Terry Lindqvist</p>
      <p class="contact__phone">tel.0427 783160</p>
    </section>

    <div class="web-band">
      <p class="web-band__text">Website:www.ridgelinepaddock.net</p>
    </div>

    <div class="mail-band">
      <p class="mail-band__text">Email:ridgelinepaddock@quolmail.com.au</p>
    </div>
  </main>
</body>
</html>
```